Business Card for Consulting Company

I would need a business card for my consulting company - the company brand and logos are defined and shared as part of this project. The proposed design for the business card can be reused as inspiration for my email signature.

```html
<!DOCTYPE html>
<html lang="en">
<head>
<meta charset="utf-8">
<title>Harbourline – Business Card</title>
<link href="https://fonts.googleapis.com/css2?family=Roboto:wght@400;500;700&display=swap" rel="stylesheet">
<style>
  :root {
    --teal: #00aeac;
    --teal-deep: #009c9a;
    --ink: #1c1c1c;
    --paper: #f7f7f5;
    --backdrop: #2a2a2a;
    --rule: #9a9a9a;
  }
  * { box-sizing: border-box; margin: 0; padding: 0; }
  html, body {
    width: 1200px;
    height: 874px;
    overflow: hidden;
    background: var(--backdrop);
    font-family: "Roboto", Arial, sans-serif;
  }
  .canvas {
    position: relative;
    width: 1200px;
    height: 874px;
  }
  .card {
    position: absolute;
    left: 320px;
    width: 560px;
    height: 340px;
    border-radius: 2px;
    overflow: hidden;
  }
  .card--back {
    top: 77px;
    background: var(--teal);
    display: flex;
    align-items: center;
    justify-content: center;
  }
  .back-name {
    font-weight: 700;
    font-size: 44px;
    color: var(--teal-deep);
    letter-spacing: 0.5px;
    filter: brightness(0.9);
  }
  .card--front {
    top: 457px;
    background: var(--paper);
    display: flex;
    align-items: center;
    padding: 0 0 20px 56px;
  }
  .card--front::after {
    content: "";
    position: absolute;
    left: 0; right: 0; bottom: 0;
    height: 16px;
    background: var(--teal);
  }
  .brand {
    display: flex;
    align-items: center;
    gap: 10px;
    width: 190px;
  }
  .brand-dot {
    width: 14px;
    height: 14px;
    border-radius: 50%;
    background: var(--teal);
    flex: none;
  }
  .brand-name {
    font-weight: 700;
    font-size: 26px;
    color: var(--teal);
  }
  .divider {
    width: 1px;
    height: 100px;
    background: var(--rule);
    margin: 0 22px 0 14px;
  }
  .contact { color: var(--ink); }
  .contact-name {
    font-weight: 700;
    font-size: 20px;
    color: var(--teal);
  }
  .contact-role {
    font-weight: 500;
    font-size: 13px;
    margin: 2px 0 10px;
  }
  .contact-line {
    display: flex;
    align-items: center;
    gap: 8px;
    font-size: 12.5px;
    line-height: 18px;
  }
  .contact-line svg {
    width: 11px;
    height: 11px;
    fill: var(--teal);
    flex: none;
  }
</style>
</head>
<body>
<main class="canvas">
  <section class="card card--back" aria-label="Card back">
    <span class="back-name">Harbourline</span>
  </section>

  <section class="card card--front" aria-label="Card front">
    <div class="brand">
      <span class="brand-dot"></span>
      <span class="brand-name">Harbourline</span>
    </div>
    <div class="divider"></div>
    <div class="contact">
      <p class="contact-name">Mathis Verlaine</p>
      <p class="contact-role">Founder &amp; CEO</p>
      <p class="contact-line">
        <svg viewBox="0 0 24 24" aria-hidden="true"><path d="M6.6 10.8a15.1 15.1 0 0 0 6.6 6.6l2.2-2.2c.3-.3.7-.4 1-.2 1.1.4 2.3.6 3.6.6.6 0 1 .4 1 1V20c0 .6-.4 1-1 1C10.6 21 3 13.4 3 4c0-.6.4-1 1-1h3.5c.6 0 1 .4 1 1 0 1.3.2 2.5.6 3.6.1.3 0 .7-.2 1z"/></svg>
        +41 79 000 12 34
      </p>
      <p class="contact-line">
        <svg viewBox="0 0 24 24" aria-hidden="true"><path d="M2 5h20v14H2zM4 7v.5l8 5 8-5V7l-8 5z"/></svg>
        mathis.v@harbourline.ch
      </p>
      <p class="contact-line">
        <svg viewBox="0 0 24 24" aria-hidden="true"><circle cx="12" cy="12" r="10"/></svg>
        www.harbourline.ch
      </p>
    </div>
  </section>
</main>
</body>
</html>
```